Graphical book cover for the book Kaffe, Ost og Gæster (Coffee, Cheese and Guests)

We need a book cover for our book Called Kaffe, Ost og Gæster with the subtitle "Vejen gennem det nordiske kaffe og ostehåndværk" In English that is "Coffee, Cheese and Guests - The path through the nordic coffee and cheesecraft" We want a design with graphics not pictures. Like the infographic way and a little rustic. Our basis colors are light brown(RGB190/183/165) and dark brown(RGB 59/33/17), but we are open for suggestions. We really like the one Te & Brød side om side in our enclosed collage, but we do not want to copy them, but we want that kind of style. It is in the same market, so we cannot be seens as copycats. You can our webpage with infographics her http://kaffeostgaester.dk/infographics/
Our webpage is http://kaffeostgaester.dk
Size of book is 26 cm high and 21cm wide.

Beer loving couples, beer lovers, travel lovers

• Should not look like a traditional beer label

```html
<!DOCTYPE html>
<html lang="da">
<head>
<meta charset="utf-8">
<title>Kaffe, Ost og Gæster – bogomslag</title>
<link rel="stylesheet" href="https://fonts.googleapis.com/css2?family=Open+Sans:wght@400&family=Kaushan+Script&family=Arimo:wght@400&display=swap">
<style>
  :root {
    --page-bg: #ffffff;
    --cover-brown: #3b2111;
    --cover-brown-deep: #2e190c;
    --spine-grey: #bab5a7;
    --light-brown: #beb7a5;
    --frame-line: #8a4a25;
    --badge-brown: #7a5a3e;
    --band-dark: rgba(30, 14, 5, 0.55);
    --subtitle-text: #d9d1c1;
    --foam-cream: #fbf3dc;
    --amber: #f7a51c;
    --amber-deep: #f08a12;
  }
  * { margin: 0; padding: 0; box-sizing: border-box; }
  html, body {
    width: 1200px;
    height: 900px;
    overflow: hidden;
    background: var(--page-bg);
  }
  .book-cover {
    position: absolute;
    left: 233px;
    top: 0;
    width: 732px;
    height: 900px;
    background: radial-gradient(ellipse at 55% 40%, var(--cover-brown) 0%, var(--cover-brown-deep) 100%);
    overflow: hidden;
  }
  .spine-strip {
    position: absolute;
    left: 0;
    top: 0;
    width: 44px;
    height: 100%;
    background: var(--spine-grey);
  }
  .inner-frame {
    position: absolute;
    left: 44px;
    top: 14px;
    right: 14px;
    bottom: 10px;
    border: 1px solid var(--frame-line);
  }
  .hops-illustration {
    position: absolute;
    left: 420px;
    top: 14px;
    width: 180px;
    height: 170px;
    background: radial-gradient(circle at 50% 55%, #241208 0%, rgba(36, 18, 8, 0) 72%);
  }
  .title-main {
    position: absolute;
    left: 90px;
    top: 90px;
    width: 470px;
    height: 320px;
  }
  .title-main text {
    font-family: "Open Sans", Arial, sans-serif;
    font-size: 180px;
    font-weight: 400;
  }
  .amp-badge {
    position: absolute;
    left: 562px;
    top: 330px;
    width: 122px;
    height: 122px;
    border-radius: 50%;
    background: var(--badge-brown);
    color: var(--light-brown);
    font-family: "Arimo", Arial, sans-serif;
    font-size: 58px;
    line-height: 122px;
    text-align: center;
  }
  .title-secondary {
    position: absolute;
    left: 0;
    top: 448px;
    width: 726px;
    text-align: center;
    font-family: "Kaushan Script", cursive;
    font-size: 80px;
    font-weight: 400;
    color: var(--light-brown);
    line-height: 1;
  }
  .drinks-illustration {
    position: absolute;
    left: 182px;
    top: 640px;
    width: 355px;
    height: 249px;
    background: linear-gradient(100deg, #e8952e 0%, #c96a18 50%, #4a2410 68%, #2a1308 100%);
    border-radius: 20px 20px 0 0;
  }
  .subtitle-band {
    position: absolute;
    left: 75px;
    top: 546px;
    width: 620px;
    height: 71px;
    background: var(--band-dark);
    color: var(--subtitle-text);
    font-family: "Arimo", Arial, sans-serif;
    font-size: 23px;
    line-height: 71px;
    text-align: center;
    letter-spacing: 0.3px;
  }
</style>
</head>
<body>
  <main class="book-cover">
    <div class="spine-strip"></div>
    <div class="inner-frame"></div>

    <div class="hops-illustration" role="img" aria-label="Illustration of hop cones and grain stalks in dark line art"></div>

    <svg class="title-main" viewBox="0 0 470 320" aria-label="Kaffe">
      <defs>
        <linearGradient id="title-fill" x1="0" y1="0" x2="0" y2="1">
          <stop offset="0" stop-color="var(--foam-cream)"/>
          <stop offset="0.35" stop-color="#fbe3a4"/>
          <stop offset="0.5" stop-color="var(--amber-deep)"/>
          <stop offset="1" stop-color="var(--amber)"/>
        </linearGradient>
      </defs>
      <text x="232" y="305" text-anchor="middle" fill="url(#title-fill)">Kaffe</text>
    </svg>

    <div class="amp-badge">&amp;</div>

    <h1 class="title-secondary">Ost og Gæster</h1>

    <div class="drinks-illustration" role="img" aria-label="Illustration of a foaming mug and a brown bottle"></div>

    <p class="subtitle-band">Vejen gennem det nordiske kaffe og ostehåndværk</p>
  </main>
</body>
</html>
```